AV & Engineering company needs a Business Card Design

Like the simple design, don't too colorful. Smart & professional feel

• I would like to see the vertical design.

```html
<!DOCTYPE html>
<html lang="en">
<head>
<meta charset="UTF-8">
<title>Norvale Systems Co. – Business Card</title>
<link rel="stylesheet" href="https://fonts.googleapis.com/css2?family=Open+Sans:wght@400;600;700&display=swap">
<style>
  :root {
    --backdrop: #3b332f;
    --card-dark: #0c0c0d;
    --card-light: #ffffff;
    --brand-red: #9e2528;
    --steel-grey: #5b5e63;
    --text-dark: #1e1e1e;
    --text-light: #ffffff;
  }
  * { margin: 0; padding: 0; box-sizing: border-box; }
  html, body {
    width: 1200px;
    height: 768px;
    overflow: hidden;
  }
  body {
    background: var(--backdrop);
    font-family: "Open Sans", Arial, sans-serif;
    position: relative;
  }
  .card {
    position: absolute;
    top: 134px;
    width: 286px;
    height: 500px;
    overflow: hidden;
    box-shadow: 0 8px 22px rgba(0,0,0,0.45);
  }
  .card-front { left: 274px; background: var(--card-dark); }
  .card-back  { left: 640px; background: var(--card-light); }

  .card-art {
    position: absolute;
    inset: 0;
    width: 100%;
    height: 100%;
  }

  .brand {
    position: absolute;
    display: flex;
    align-items: center;
    gap: 10px;
    color: var(--brand-red);
    font-weight: 700;
    text-transform: uppercase;
    letter-spacing: 0.5px;
    line-height: 1.15;
  }
  .brand-mark {
    flex: none;
    background: var(--brand-red);
  }
  .card-front .brand {
    left: 0;
    right: 0;
    top: 220px;
    justify-content: center;
    font-size: 21px;
  }
  .card-front .brand-mark { width: 24px; height: 24px; }
  .card-back .brand { left: 28px; top: 40px; font-size: 18px; }
  .card-back .brand-mark { width: 18px; height: 18px; }

  .contact-list {
    position: absolute;
    left: 28px;
    top: 118px;
    list-style: none;
    font-size: 12px;
    color: var(--text-dark);
    line-height: 22px;
  }
  .contact-list li { display: flex; align-items: center; gap: 8px; }
  .contact-icon { width: 11px; height: 11px; fill: var(--brand-red); flex: none; }
  .web-accent { color: var(--brand-red); }

  .person {
    position: absolute;
    right: 26px;
    bottom: 34px;
    text-align: right;
    color: var(--text-light);
  }
  .person-name { font-size: 16px; font-weight: 700; }
  .person-role { font-size: 12px; font-weight: 400; margin-top: 2px; }
</style>
</head>
<body>

  <section class="card card-front" aria-label="Card front">
    <svg class="card-art" viewBox="0 0 286 500" preserveAspectRatio="none">
      <polygon points="196,0 286,0 286,24 208,24" fill="var(--brand-red)"/>
      <polygon points="0,462 82,462 94,480 0,480" fill="var(--steel-grey)"/>
    </svg>
    <div class="brand"><span class="brand-mark"></span><span>Norvale Systems<br>Co.</span></div>
  </section>

  <section class="card card-back" aria-label="Card back">
    <svg class="card-art" viewBox="0 0 286 500" preserveAspectRatio="none">
      <path d="M0,300 C70,350 170,366 286,346 L286,358 C170,378 70,362 0,312 Z" fill="var(--steel-grey)"/>
      <path d="M0,326 C70,380 160,394 286,376 L286,500 L0,500 Z" fill="var(--brand-red)"/>
    </svg>

    <div class="brand"><span class="brand-mark"></span><span>Norvale Systems<br>Co.</span></div>

    <ul class="contact-list">
      <li>
        <svg class="contact-icon" viewBox="0 0 12 12"><path d="M6 0a4 4 0 0 0-4 4c0 3 4 8 4 8s4-5 4-8a4 4 0 0 0-4-4zm0 5.5A1.5 1.5 0 1 1 6 2.5a1.5 1.5 0 0 1 0 3z"/></svg>
        Your Commercial or office address
      </li>
      <li>
        <svg class="contact-icon" viewBox="0 0 12 12"><path d="M1 4c0-2 2-3 5-3s5 1 5 3v1H8V4H4v1H1zM3 6h6l1 5H2z"/></svg>
        00.00.00.0000
      </li>
      <li>
        <svg class="contact-icon" viewBox="0 0 12 12"><path d="M3 0h6v4H3zM1 5h10v7H1zm2 2v1h2V7zm4 0v1h2V7zM3 9v1h2V9zm4 0v1h2V9z"/></svg>
        00.00.00.0000
      </li>
      <li>
        <svg class="contact-icon" viewBox="0 0 12 12"><path d="M0 2h12v8H0zm1 1v.5l5 3.5 5-3.5V3z"/></svg>
        yourname@yourwebsite.com
      </li>
      <li>
        <svg class="contact-icon" viewBox="0 0 12 12"><path d="M6 0a6 6 0 1 0 0 12A6 6 0 0 0 6 0zm4.9 5.3H8.6A9 9 0 0 0 7.5 1.3a5 5 0 0 1 3.4 4zM6 1.2c.7.9 1.3 2.3 1.4 4.1H4.6C4.7 3.5 5.3 2.1 6 1.2zM4.5 1.3a9 9 0 0 0-1.1 4H1.1a5 5 0 0 1 3.4-4zM1.1 6.7h2.3a9 9 0 0 0 1.1 4 5 5 0 0 1-3.4-4zM6 10.8c-.7-.9-1.3-2.3-1.4-4.1h2.8c-.1 1.8-.7 3.2-1.4 4.1zm1.5-.1a9 9 0 0 0 1.1-4h2.3a5 5 0 0 1-3.4 4z"/></svg>
        <span>www.<span class="web-accent">yourwebsite</span>.com</span>
      </li>
    </ul>

    <div class="person">
      <div class="person-name">Your Long Name</div>
      <div class="person-role">Managing Director</div>
    </div>
  </section>

</body>
</html>
```